Church needs a graphic design/flyer layout for upcoming series

I need a multi-purpose design for promoting both our upcoming series of messages and our fall kick-off event where we will launch the messages.

Our promotion will be printed on a two-sided. One side is simple and focuses on the series and the other side has details in regards to the event. I have provided an attachment example of what we did last time.

The design needs to be multi-purpose because it will be used for our sermon Power Points, placed on our website banner, social media, etc.

• Sermon series is called “Harbor Lanterns”
• The subtitle will be “What’s keeping you from God?”
• Our name logo should be on the graphic as well.
• The subject manner will revolve around common hurdles that people face about God and Christianity: The existence of God, the exclusivity of religion, Hell, the reliability of the Bible, Hypocrisy in the church, etc.
• Our mission is “Connecting Young Families to Christ” so our focus is to reach out to families while not being exclusive to others.
• Our target audience is families with school-aged kids.
• This series is an invitational focus so we want it to be appealing to non-church goers.
• It should be attention grabbing while not being too ‘edgy’

• The front of the card will most likely consist the Sermon Series Graphic, title & subtitle of the series, and perhaps our name logo somewhere on it.
• The back of the card will invite and give the basic information for the event so that the people will be encouraged to save the date and come to the event.
• Here are some things that could be included on that advertisement:
o The name of the event: “Westbrook Commons Open Day”
o The date and time of the event: Sept 23rd @ 10:30
o Features of the event:
 Free lunch
 Children’s program
 Bouncy Castle
 Start of the “Harbor Lanterns” messages.
 Sample of topics
o Information about the church: our website and address, etc
o Engaging pictures and graphics.
• The rest of the tone and manner are the same as the sermon series graphic.
The flyer will be 11X14, like a postcard size.

Target Market(s)

Young families who are spiritually curious but not committed church attenders.

Colors

Designer to choose colors to be used in the design.

Requirements
Nice to have
• A modern and professional looking design.
Should not have
• Anything offensive or not family friendly.

```html
<!DOCTYPE html>
<html lang="en">
<head>
<meta charset="utf-8">
<title>Harbor Lanterns – Westbrook Commons Open Day</title>
<link href="https://fonts.googleapis.com/css2?family=Lato:wght@400;700;900&display=swap" rel="stylesheet">
<style>
  :root {
    --backdrop-light: #e8e8ea;
    --backdrop-dark: #2d2d2f;
    --purple: #8f2a8d;
    --purple-deep: #6e1f6d;
    --purple-edge: #7a2379;
    --white: #ffffff;
    --ink: #3a3a3c;
    --sky-top: #3b3580;
    --sky-mid: #8a4a86;
    --sky-glow: #d06a5c;
    --sky-ground: #2a1a22;
    --night-top: #1f2448;
    --night-mid: #4a5070;
    --night-low: #6a4a58;
  }
  * { box-sizing: border-box; margin: 0; padding: 0; }
  html, body { width: 1200px; height: 509px; overflow: hidden; }
  body {
    font-family: "Lato", sans-serif;
    background: linear-gradient(to bottom, var(--backdrop-light) 0 318px, var(--backdrop-dark) 318px 100%);
    position: relative;
  }
  .card {
    position: absolute;
    top: 50px;
    width: 522px;
    height: 410px;
    overflow: hidden;
    box-shadow: 0 2px 6px rgba(0,0,0,.25);
  }
  .card--front { left: 64px; }
  .card--back { left: 614px; background: var(--purple); }

  /* Front */
  .series-photo {
    position: absolute; inset: 0;
    background: linear-gradient(to bottom, var(--sky-top) 0%, var(--sky-mid) 35%, var(--sky-glow) 68%, #b8503e 82%, var(--sky-ground) 100%);
  }
  .name-banner { position: absolute; left: 148px; top: 0; width: 226px; height: 132px; }
  .name-banner__inner {
    position: absolute; left: 148px; top: 0; width: 226px; height: 110px;
    display: flex; flex-direction: column; align-items: center; justify-content: center; gap: 8px;
  }
  .name-mark { width: 48px; height: 48px; border-radius: 50%; background: var(--purple); }
  .church-name { font-size: 15px; font-weight: 400; color: var(--ink); white-space: nowrap; }
  .series-title {
    position: absolute; left: 0; right: 0; top: 146px;
    text-align: center; color: var(--white);
    font-size: 44px; font-weight: 900; letter-spacing: .5px; text-transform: uppercase;
    text-shadow: 0 2px 4px rgba(0,0,0,.35);
  }
  .series-subtitle {
    position: absolute; left: 0; right: 0; top: 202px;
    text-align: center; color: var(--white); font-size: 18px; font-weight: 700;
    text-shadow: 0 1px 3px rgba(0,0,0,.35);
  }

  /* Back */
  .event-photo {
    position: absolute; left: 0; right: 0; top: 100px; height: 230px;
    background: linear-gradient(to bottom, var(--night-top) 0%, var(--night-mid) 45%, var(--night-low) 80%, #3a2430 100%);
  }
  .bands { position: absolute; inset: 0; }
  .event-title {
    position: absolute; left: 0; right: 0; top: 46px; text-align: center;
    color: var(--white); font-size: 30px; font-weight: 700; white-space: nowrap;
  }
  .event-date {
    position: absolute; left: 0; right: 0; top: 92px; text-align: center;
    color: var(--white); font-size: 16px; font-weight: 700;
  }
  .features { position: absolute; left: 30px; top: 162px; color: var(--white); }
  .features__heading { font-size: 19px; font-weight: 700; margin-bottom: 6px; }
  .features__list { list-style: none; }
  .features__list li {
    font-size: 14.5px; font-weight: 700; line-height: 19px; padding-left: 17px; position: relative;
  }
  .features__list li::before {
    content: ""; position: absolute; left: 0; top: 6px; width: 7px; height: 7px; border-radius: 50%; background: var(--white);
  }
  .name-tab { position: absolute; left: 312px; top: 174px; width: 211px; height: 106px; }
  .name-tab__inner {
    position: absolute; left: 326px; top: 174px; width: 197px; height: 106px;
    display: flex; flex-direction: column; align-items: center; justify-content: center; gap: 7px;
  }
  .name-tab__inner .church-name { font-size: 13.5px; }
  .name-tab__inner .name-mark { width: 46px; height: 46px; }
  .contact { position: absolute; left: 0; right: 0; top: 326px; text-align: center; color: var(--white); }
  .contact__phone { font-size: 24px; font-weight: 700; margin-bottom: 4px; }
  .contact__line { font-size: 11px; font-weight: 700; line-height: 15px; }
</style>
</head>
<body>
  <section class="card card--front">
    <div class="series-photo" role="img" aria-label="Sunset sky over a field with a row of families holding hands in silhouette"></div>
    <svg class="name-banner" viewBox="0 0 226 132" aria-hidden="true">
      <polygon points="0,0 226,0 226,110 113,132 0,110" fill="var(--white)" stroke="var(--purple)" stroke-width="3"/>
    </svg>
    <div class="name-banner__inner">
      <span class="name-mark"></span>
      <span class="church-name">Maple Hollow Family Church</span>
    </div>
    <h1 class="series-title">Harbor Lanterns</h1>
    <p class="series-subtitle">What’s keeping you from God?</p>
  </section>

  <section class="card card--back">
    <div class="event-photo" role="img" aria-label="Evening sky with streaks of cloud"></div>
    <svg class="bands" viewBox="0 0 523 410" preserveAspectRatio="none" aria-hidden="true">
      <polygon points="0,0 523,0 523,116 261,150 0,116" fill="var(--purple-edge)"/>
      <polygon points="0,0 523,0 523,110 261,144 0,110" fill="var(--purple)"/>
      <polygon points="0,318 261,294 523,318 523,410 0,410" fill="var(--purple-edge)"/>
      <polygon points="0,326 261,300 523,326 523,410 0,410" fill="var(--purple)"/>
    </svg>
    <h2 class="event-title">Westbrook Commons Open Day</h2>
    <p class="event-date">Sept 23rd @ 10:30</p>
    <div class="features">
      <h3 class="features__heading">Features of the event:</h3>
      <ul class="features__list">
        <li>Free lunch</li>
        <li>Children’s program</li>
        <li>Bouncy Castle</li>
        <li>Start of the “Harbor Lanterns” messages.</li>
        <li>Sample of topics</li>
      </ul>
    </div>
    <svg class="name-tab" viewBox="0 0 211 106" aria-hidden="true">
      <polygon points="14,0 211,0 211,106 14,106 0,53" fill="var(--white)"/>
    </svg>
    <div class="name-tab__inner">
      <span class="name-mark"></span>
      <span class="church-name">Maple Hollow Family Church</span>
    </div>
    <div class="contact">
      <p class="contact__phone">Ph: 555.014.2287</p>
      <p class="contact__line">Location: 1180 Birchwood Road East, Lakeview, ON A1B 2C3</p>
      <p class="contact__line">Email: info@maplehollowchurch.ca | Website: www.maplehollowchurch.ca</p>
    </div>
  </section>
</body>
</html>
```